Conveyancing flyer

We need a flyer design for a new service we are offering. Dwellquarter.co.uk is launching its own conveyancing business called Keystone Counsel.

It has a strapline of 'Committed to helping you move'

Bullet points of the key features of the service are:-

* Hand-picked team of expert lawyers
• Fixed fees
• Capacity management
• Faster times to exchange of contracts
• More certainty and less stress

We need a large call now area and it should fit our branding which you can within our website, in particular with the colours of our logo.

Ideally we would like an area on the back to summarise the service in a little more details. So would need a text area as will. This area would be labelled 'Taking the guesswork out of dining the right lawyer'

The flyer should be double sized and a5

Please note this requirement is an A5 flyer double sided, not just the front. Please resubmit if you have designed differently.

```html
<!DOCTYPE html>
<html lang="en">
<head>
<meta charset="utf-8">
<title>Keystone Counsel – Conveyancing Flyer</title>
<link rel="stylesheet" href="https://fonts.googleapis.com/css2?family=Signika:wght@400;600&family=Arimo:wght@400;700&display=swap">
<style>
:root{
  --pink:#e9489a;
  --cyan:#1bb7e3;
  --dark:#2e2e30;
  --darker:#242426;
  --grey-light:#dcdcdc;
  --grey-mid:#a9a9ab;
  --text-light:#f1f1f1;
  --canvas:#ece9e4;
}
*{margin:0;padding:0;box-sizing:border-box}
html,body{width:1200px;height:1000px;overflow:hidden}
body{background:var(--canvas);position:relative;font-family:"Arimo",Arial,sans-serif}
.page{position:absolute;top:155px;width:490px;height:695px;background:var(--dark);overflow:hidden;box-shadow:0 2px 10px rgba(0,0,0,.25)}
.page-front{left:93px}
.page-back{left:645px}

/* brand */
.brand{display:flex;align-items:center;gap:8px;font-family:"Signika",sans-serif;font-weight:400;color:var(--pink)}
.brand-mark{width:16px;height:16px;background:var(--pink)}

/* front */
.front-header{position:absolute;left:0;top:0;width:490px;height:78px;background:linear-gradient(#e6e6e6,#cfcfcf)}
.front-header .brand{position:absolute;left:22px;top:24px;font-size:27px}
.rule-pink{position:absolute;left:0;width:490px;height:4px;background:var(--pink)}
.photo-family{position:absolute;left:0;top:84px;width:490px;height:350px;background:linear-gradient(160deg,#efe8de 0%,#d8bf9c 45%,#b98b5c 100%)}
.headline{position:absolute;right:0;top:100px;width:230px;height:76px;background:var(--cyan);color:#fff;font-family:"Signika",sans-serif;font-size:22px;line-height:26px;text-align:center;padding-top:12px}
.services{position:absolute;left:0;top:332px;width:232px;height:93px;background:rgba(40,40,40,.72);padding:6px 0 0 24px;color:#fff}
.services h2{font-family:"Signika",sans-serif;font-weight:400;color:var(--cyan);font-size:16px;margin-bottom:2px}
.services ul{list-style:none;font-size:9.5px;line-height:12.7px}
.services li::before{content:"• "}
.strap-band{position:absolute;left:0;top:437px;width:490px;height:33px;background:var(--pink);color:#fff;font-family:"Signika",sans-serif;font-size:17px;text-align:center;line-height:33px;box-shadow:0 -3px 0 #fff,0 3px 0 #fff}
.contact{position:absolute;left:16px;top:498px;color:var(--text-light)}
.contact h3{font-size:10px;font-weight:700;margin-bottom:12px}
.contact-row{display:flex;align-items:flex-start;gap:10px;height:47px}
.contact-icon{width:42px;height:42px;flex:none}
.contact-row p{font-size:9.5px;line-height:12px;width:130px;padding-top:4px}
.divider-v{position:absolute;left:222px;top:530px;width:1px;height:90px;background:#666}
.service-copy{position:absolute;left:241px;top:509px;width:232px;color:var(--text-light)}
.service-copy h3{font-size:11px;font-weight:700;margin-bottom:14px}
.service-copy p{font-size:9.5px;line-height:11.8px}
.foot-stripes{position:absolute;left:0;bottom:0;width:490px;height:12px;background:linear-gradient(#bdbdbd 0 4px,var(--darker) 4px 6px,var(--pink) 6px 8px,#d4d4d4 8px)}

/* back */
.photo-office{position:absolute;left:0;top:0;width:490px;height:363px;background:linear-gradient(90deg,#dfe4e8 0%,#b7c2cb 40%,#4c525a 60%,#3b4048 100%)}
.back-brand-box{position:absolute;left:15px;top:73px;width:203px;height:77px;background:rgba(255,255,255,.85);box-shadow:0 2px 6px rgba(0,0,0,.2)}
.back-brand-box .brand{position:absolute;left:12px;top:26px;font-size:19px}
.title-band{position:absolute;left:0;top:367px;width:490px;height:31px;background:var(--pink);color:#fff;font-family:"Signika",sans-serif;font-size:15px;text-align:center;line-height:31px;box-shadow:0 -3px 0 #fff,0 3px 0 #fff}
.summary{position:absolute;left:22px;top:420px;width:455px;color:var(--text-light);font-size:8.9px;line-height:11.05px}
.summary .drop{font-size:15px;line-height:9px}
.summary-rule{position:absolute;left:120px;top:662px;width:250px;height:1px;background:#555}
</style>
</head>
<body>

<section class="page page-front" aria-label="Flyer front">
  <header class="front-header">
    <div class="brand"><span class="brand-mark"></span>Dwellquarter.co.uk</div>
  </header>
  <div class="rule-pink" style="top:78px"></div>
  <div class="photo-family" role="img" aria-label="Photo of a smiling family lying on the floor among moving boxes with a sold sign"></div>
  <div class="headline">Conveyancing made<br>quick and easy</div>
  <div class="services">
    <h2>Our Services Include :</h2>
    <ul>
      <li>Hand-picked team of expert lawyers</li>
      <li>Fixed fees</li>
      <li>Capacity management</li>
      <li>Faster times to exchange of contracts</li>
      <li>More certainty and less stress</li>
    </ul>
  </div>
  <div class="strap-band">Committed to helping you move</div>

  <div class="contact">
    <h3>Contact :</h3>
    <div class="contact-row">
      <svg class="contact-icon" viewBox="0 0 42 42"><circle cx="21" cy="21" r="21" fill="#111"/><path d="M21 10a7 7 0 0 0-7 7c0 5 7 13 7 13s7-8 7-13a7 7 0 0 0-7-7z" fill="#fff"/><circle cx="21" cy="17" r="2.6" fill="#111"/></svg>
      <p>Estate Offices, Units 4 &amp; 4a, Millbrook Lane, Thornbury, Essex CM9 2XY</p>
    </div>
    <div class="contact-row">
      <svg class="contact-icon" viewBox="0 0 42 42"><circle cx="21" cy="21" r="21" fill="#111"/><path d="M13 12l5-1 3 6-3 2c1 3 3 5 6 6l2-3 6 3-1 5c-9 1-19-9-18-18z" fill="#fff"/></svg>
      <p>FREEPHONE: 0800 555 0148</p>
    </div>
    <div class="contact-row">
      <svg class="contact-icon" viewBox="0 0 42 42"><circle cx="21" cy="21" r="21" fill="#111"/><g fill="none" stroke="#fff" stroke-width="1.6"><circle cx="21" cy="21" r="10"/><ellipse cx="21" cy="21" rx="4.5" ry="10"/><path d="M11 21h20M13 15h16M13 27h16"/></g></svg>
      <p style="padding-top:14px">http://www.dwellquarter.co.uk/</p>
    </div>
  </div>
  <div class="divider-v"></div>
  <div class="service-copy">
    <h3>Guaranteed Personal Service</h3>
    <p>Yes we're the original online estate agents. Yes we've saved our customers over £40 million in fees. Yes we've won awards and been featured on TV &amp; radio, but it's our comprehensive service that makes us stand out from the crowd. From free market appraisals, one to one account manager, sales progression &amp; completion, we're your 21st century estate agent. Why risk a private house sale or use a cheap imitation? Join the thousands that have saved thousands with the best online estate agent.</p>
  </div>
  <div class="foot-stripes"></div>
</section>

<section class="page page-back" aria-label="Flyer back">
  <div class="photo-office" role="img" aria-label="Photo of a lawyer in a grey suit with folded arms in a blurred meeting room"></div>
  <div class="back-brand-box">
    <div class="brand"><span class="brand-mark"></span>Dwellquarter.co.uk</div>
  </div>
  <div class="title-band">Taking The Guesswork Out Of Finding The Right Lawyer</div>
  <div class="summary">
    <p><span class="drop">I</span>nstructing the right lawyer can be the difference between a quick, trouble-free move or a long and stressful one. In some cases it can even be the difference between completing or not.</p>
    <p>Finding the right lawyer is becoming increasingly more difficult as most law firms all seem to promise the same things these days. In the absence of any real differentiators many people either choose their lawyer based simply upon price or location.</p>
    <p>Generally speaking, cheap legal fees are only achievable by firms which employ unqualified, inexperienced conveyancers and in our experience these firms are very often the reason for unnecessary hold ups. Experienced, qualified lawyers are generally better placed to look after you. However, we have found that good lawyers are very often the victims of their own success and will quickly attract and take on more work than they can handle. Rarely will you ever hear a lawyer turning down work and an overworked lawyer can be as frustrating and problematic as an inexperienced one.</p>
    <p>At Dwellquarter we recognise the importance of having a good lawyer by your side during this time and so we have employed our very own ex-property lawyer to identify and manage a nationwide team of the best lawyers that we can find. We continually work with this team to improve service standards, simplify the process and most importantly, to ensure that these lawyers do not take on more work than they can handle.</p>
    <p>In short, this allows us to be able to offer an enhanced and exclusive legal service to buyers and sellers alike. All of our lawyers work on the same, fixed fees and always on a no sale / no fee basis which in turn ensures a pragmatic and proactive approach.</p>
    <p>Ultimately this means that we are able to provide our buyers and sellers with more certainty, less stress and faster times to exchange of contracts.</p>
  </div>
  <div class="summary-rule"></div>
  <div class="foot-stripes"></div>
</section>

</body>
</html>
```